Business Card Design for Translation Company - Rush

Rush job for a business card designing for a company doing international translations, several Asian and western languages. Already have a logo design (see attached) to use as the basis of the business card design. For the card, we also need the full company name, address, email, and phone number. In addition, my name as I will be the one handing out the cards.

For the logo design, we think the white background would be best. But we will consider using the dark background if you have a great idea for it.

The attached jpeg design has just been approved, but the designer has not yet finalized the file. When we select our final applicant, we will send the finalized file. (Nothing changes except the quality of the data.)

The phone number may change and if so, we will send the new one when we select our applicant.

We must complete the entire process and have a design ready to go to print no later than 01:00 am August 3, New York (East Coast) time.

We look forward to your participation in the project,
Gus

Target Market(s)

Translation clients worldwide.

Industry/Entity Type

Business

Contact Information for Business Card

Company details:

Korvani Languages Worldwide, Ltd.

#527-2368 Halden Crescent, Victoria, BC, Canada V9T3K2

gdresner@korvanilanguages.example

+1-888-604-2731

Font styles to use
Sans Serif

Requirements
Must have
• Company name, address, email and phone number.
• Also my name:
• Gustav R. Dresner
• Director
Nice to have
• Not a demand, but please consider creatively using the horizontal bar.
Should not have
• Cluttered of jumbled appearance.

```html
<!DOCTYPE html>
<html lang="en">
<head>
<meta charset="utf-8">
<title>Korvani Languages Worldwide – Business Card</title>
<link rel="stylesheet" href="https://fonts.googleapis.com/css2?family=Montserrat:wght@400;600;700&display=swap">
<style>
  :root {
    --backdrop: #bcbdbf;
    --card-dark: #181818;
    --card-light: #ffffff;
    --orange: #f07f22;
    --charcoal: #434345;
    --ink: #333335;
    --shade: rgba(0,0,0,0.35);
  }
  html, body {
    margin: 0;
    width: 1200px;
    height: 1000px;
    overflow: hidden;
    background: var(--backdrop);
    font-family: "Montserrat", Arial, sans-serif;
  }
  .canvas { position: relative; width: 1200px; height: 1000px; }
  .card {
    position: absolute;
    left: 271px;
    width: 658px;
    height: 385px;
    overflow: hidden;
    box-shadow: 4px 5px 4px var(--shade);
  }
  .card--front { top: 81px; background: var(--card-dark); }
  .card--back { top: 535px; background: var(--card-light); }

  .brand { position: absolute; display: flex; align-items: center; }
  .brand__dot { border-radius: 50%; background: var(--orange); flex: none; }
  .brand__name {
    display: grid;
    font-weight: 600;
    text-transform: uppercase;
    line-height: 1.3;
    white-space: nowrap;
  }
  .brand__line { display: flex; align-items: center; }
  .brand__bar { flex: 1; height: 3px; background: var(--orange); margin-left: 10px; min-width: 0; }

  .card--front .brand { left: 89px; top: 149px; }
  .card--front .brand__dot { width: 80px; height: 80px; margin-right: 30px; }
  .card--front .brand__name { color: #ffffff; font-size: 22px; letter-spacing: 4.6px; }

  .card--back .brand { left: 30px; right: 0; top: 40px; }
  .card--back .brand__dot { width: 64px; height: 64px; margin-right: 28px; }
  .card--back .brand__name { flex: 1; grid-template-columns: 1fr; color: var(--charcoal); font-size: 16px; letter-spacing: 3.2px; }

  .stripes { position: absolute; left: 0; top: 157px; }
  .stripe { position: absolute; left: 0; height: 3px; }
  .stripe--orange { background: var(--orange); }
  .stripe--dark { background: var(--charcoal); }

  .person { position: absolute; right: 40px; top: 168px; text-align: right; }
  .person__name { margin: 0 0 4px; font-size: 18px; font-weight: 700; color: var(--ink); }
  .person__title { margin: 0; font-size: 12px; font-weight: 600; letter-spacing: 2.5px; text-transform: uppercase; color: var(--orange); }

  .contact { position: absolute; left: 41px; top: 270px; color: var(--ink); }
  .contact__company { margin: 0 0 8px; font-size: 15px; font-weight: 700; }
  .contact__list { list-style: none; margin: 0; padding: 0; font-size: 13px; }
  .contact__item { display: flex; align-items: center; height: 21px; }
  .contact__icon { width: 15px; height: 15px; margin-right: 7px; flex: none; }
</style>
</head>
<body>
<main class="canvas">
  <section class="card card--front" aria-label="Card front">
    <div class="brand">
      <span class="brand__dot"></span>
      <span class="brand__name">
        <span class="brand__line">Korvani<span class="brand__bar"></span></span>
        <span class="brand__line">Languages</span>
      </span>
    </div>
  </section>

  <section class="card card--back" aria-label="Card back">
    <div class="brand">
      <span class="brand__dot"></span>
      <span class="brand__name">
        <span class="brand__line">Korvani<span class="brand__bar"></span></span>
        <span class="brand__line">Languages</span>
      </span>
    </div>

    <div class="stripes" aria-hidden="true">
      <span class="stripe stripe--orange" style="top:0;width:357px"></span>
      <span class="stripe stripe--dark" style="top:13px;width:333px"></span>
      <span class="stripe stripe--orange" style="top:26px;width:307px"></span>
      <span class="stripe stripe--dark" style="top:39px;width:282px"></span>
      <span class="stripe stripe--orange" style="top:52px;width:257px"></span>
      <span class="stripe stripe--dark" style="top:65px;width:232px"></span>
    </div>

    <div class="person">
      <p class="person__name">Gustav R. Dresner</p>
      <p class="person__title">Director</p>
    </div>

    <div class="contact">
      <p class="contact__company">Korvani Languages Worldwide, Ltd.</p>
      <ul class="contact__list">
        <li class="contact__item">
          <svg class="contact__icon" viewBox="0 0 16 16" aria-hidden="true"><circle cx="8" cy="8" r="8" fill="#f07f22"/><path d="M5 11.5 L11 4.5" stroke="#fff" stroke-width="2" stroke-linecap="round"/></svg>
          +1-888-604-2731
        </li>
        <li class="contact__item">
          <svg class="contact__icon" viewBox="0 0 16 16" aria-hidden="true"><circle cx="8" cy="8" r="8" fill="#f07f22"/><rect x="4" y="5" width="8" height="6" fill="#fff"/><path d="M4 5 L8 8.5 L12 5" stroke="#f07f22" stroke-width="1" fill="none"/></svg>
          gdresner@korvanilanguages.example
        </li>
        <li class="contact__item">
          <svg class="contact__icon" viewBox="0 0 16 16" aria-hidden="true"><circle cx="8" cy="8" r="8" fill="#f07f22"/><path d="M8 13 C5 9 5 8 5 7 A3 3 0 0 1 11 7 C11 8 11 9 8 13 Z" fill="#fff"/><circle cx="8" cy="7" r="1.2" fill="#f07f22"/></svg>
          #527-2368 Halden Crescent, Victoria, BC, Canada V9T3K2
        </li>
      </ul>
    </div>
  </section>
</main>
</body>
</html>
```